The Juniper Coach

I am a life coach specializing in helping people with depression and bipolar disorder. I would like a nice, fun design for a business card.

```html
<!DOCTYPE html>
<html lang="en">
<head>
<meta charset="utf-8">
<title>The Juniper Coach – Business Card</title>
<link rel="stylesheet" href="https://fonts.googleapis.com/css2?family=Cinzel:wght@400;600&family=Arimo:wght@400&display=swap">
<style>
  :root {
    --stage: #3a3a3c;
    --card-dark: #0d0d0e;
    --lime: #8dc63f;
    --lime-soft: #a9d46a;
    --sky: #00bff3;
    --ink-light: #e6e6e6;
    --ink-muted: #b5b5b5;
    --white: #ffffff;
  }
  * { box-sizing: border-box; margin: 0; padding: 0; }
  html, body {
    width: 1200px; height: 782px; overflow: hidden;
    background: var(--stage);
  }
  .canvas {
    position: relative; width: 1200px; height: 782px;
  }
  .card {
    position: absolute; top: 231px; width: 560px; height: 320px;
    overflow: hidden; box-shadow: 0 6px 18px rgba(0,0,0,.45);
  }
  .card--back { left: 40px; background: var(--card-dark); }
  .card--front { left: 600px; }

  /* front */
  .front-pattern {
    position: absolute; inset: 0;
    background: radial-gradient(circle at 50% 50%, var(--lime-soft) 0%, var(--lime) 70%);
  }
  .front-name {
    position: absolute; left: 0; right: 0; top: 205px; text-align: center;
    font-family: "Cinzel", serif; font-weight: 600; font-size: 22px;
    color: var(--white); letter-spacing: 1px;
  }

  /* back */
  .holder {
    position: absolute; left: 26px; top: 26px;
    font-family: "Cinzel", serif;
  }
  .holder-name { font-size: 19px; font-weight: 400; letter-spacing: .5px; line-height: 1; }
  .holder-name .first { color: var(--lime); }
  .holder-name .last { color: var(--sky); }
  .holder-role {
    font-family: "Arimo", sans-serif; font-size: 12px; color: var(--ink-muted);
    margin-top: 3px;
  }

  .brand {
    position: absolute; left: 270px; top: 132px; width: 270px; text-align: center;
    font-family: "Cinzel", serif; font-weight: 600; font-size: 28px;
    color: var(--lime); letter-spacing: 1px; line-height: 1.1;
  }

  .contacts {
    position: absolute; left: 26px; top: 168px; list-style: none;
    font-family: "Arimo", sans-serif; font-size: 13.5px; color: var(--ink-light);
  }
  .contacts li { display: flex; align-items: center; gap: 8px; height: 18px; }
  .contacts svg { width: 11px; height: 11px; fill: var(--sky); flex: none; }

  .address {
    position: absolute; right: 44px; top: 222px; text-align: right;
    font-family: "Arimo", sans-serif; font-size: 14.5px; color: var(--ink-light);
    line-height: 1.3;
  }
  .bands { position: absolute; left: 0; bottom: 0; width: 560px; height: 80px; }
</style>
</head>
<body>
<main class="canvas">

  <section class="card card--back" aria-label="Business card, contact side">
    <div class="holder">
      <p class="holder-name"><span class="first">Dorian</span> <span class="last">Hale</span></p>
      <p class="holder-role">Managing Director</p>
    </div>

    <p class="brand">The Juniper Coach</p>

    <ul class="contacts">
      <li>
        <svg viewBox="0 0 12 12" aria-hidden="true"><path d="M2 1h3l1 3-1.5 1a7 7 0 0 0 2.5 2.5L8 6l3 1v3a1 1 0 0 1-1 1A9 9 0 0 1 1 2a1 1 0 0 1 1-1z"/></svg>
        044-555 010 234
      </li>
      <li>
        <svg viewBox="0 0 12 12" aria-hidden="true"><path d="M3.5 0h5a1 1 0 0 1 1 1v10a1 1 0 0 1-1 1h-5a1 1 0 0 1-1-1V1a1 1 0 0 1 1-1zm0 1.5v8h5v-8z"/></svg>
        044-555 010 234
      </li>
      <li>
        <svg viewBox="0 0 12 12" aria-hidden="true"><path d="M0 2h12v8H0zm1 1v.4l5 3.3 5-3.3V3zm0 1.6V9h10V4.6L6 7.9z"/></svg>
        hello@junipercoach.com
      </li>
      <li>
        <svg viewBox="0 0 12 12" aria-hidden="true"><circle cx="6" cy="6" r="5.5"/><path d="M6 .5v11M.5 6h11" stroke="#0d0d0e" stroke-width="1" fill="none"/></svg>
        www.junipercoach.com
      </li>
    </ul>

    <p class="address">48 Linden Row, Suite 2<br>Fairhaven, 204816</p>

    <svg class="bands" viewBox="0 0 560 80" aria-hidden="true">
      <polygon points="0,26 262,26 250,42 0,42" fill="var(--lime)"/>
      <polygon points="258,52 560,52 560,80 238,80" fill="var(--sky)"/>
    </svg>
  </section>

  <section class="card card--front" aria-label="Business card, brand side">
    <div class="front-pattern" role="img" aria-label="Soft green background where a repeating brand motif belongs"></div>
    <p class="front-name">The Juniper Coach</p>
  </section>

</main>
</body>
</html>
```